Legal Industry Crowdsourcing Website

BriefHarbor.com will be a new crowdsourcing website. The audiences are law students and legal professionals, and individual citizens, predominantly those working for or running small businesses. The objective is to enable them to get cheap or free legal advice and opinions.

Think of it like ArtMingle.com but for lawyers. NB: BriefHarbor.com is NOT a law firm.

Do not include pictures of gavels (the wooden hammers). They are not used in the courts of England & Wales.
Updates

Target Market(s)

Legal industry, small business owners

Industry/Entity Type

Lawyer

Number of Pages Required

1 page

Requirements
Must have
• It must show the information presented in the Powerpoint file attached to the brief
• Must also show how the page appears on mobile devices.
Should not have
• Should not have:
• Pictures of gavels (the wooden hammers). They are not used in the courts of England & Wales.
• A vertical ever-scrolling design

```html
<!DOCTYPE html>
<html lang="en">
<head>
<meta charset="utf-8">
<title>BriefHarbor — Legal opinions from the crowd</title>
<link rel="stylesheet" href="https://fonts.googleapis.com/css2?family=Cinzel:wght@400;600;700&family=Open+Sans:wght@400;600&display=swap">
<style>
  :root{
    --gold:#c9962f;
    --gold-light:#d9a63a;
    --ink:#1f1d1b;
    --dark:#262322;
    --dark-2:#2f2b29;
    --cream:#f4f3f1;
    --white:#ffffff;
    --muted:#5a5754;
  }
  *{margin:0;padding:0;box-sizing:border-box}
  html,body{width:1200px;height:2429px;overflow:hidden}
  body{position:relative;background:var(--white);font-family:"Open Sans",Arial,sans-serif;color:var(--ink)}
  .cinzel{font-family:"Cinzel",Georgia,serif}

  /* header */
  .site-header{position:absolute;left:0;top:0;width:1200px;height:118px;background:var(--white);border-bottom:3px solid var(--gold)}
  .brand{position:absolute;left:81px;top:44px;display:flex;align-items:center;gap:10px;font-family:"Cinzel",Georgia,serif;font-size:24px;font-weight:600;color:var(--ink)}
  .brand-dot{width:14px;height:14px;border-radius:50%;background:var(--gold)}
  .main-nav{position:absolute;top:50px;left:0;font-family:"Cinzel",Georgia,serif;font-size:15px;font-weight:600;color:var(--ink)}
  .main-nav a{position:absolute;white-space:nowrap;text-decoration:none;color:inherit}

  /* hero */
  .hero{position:absolute;left:0;top:118px;width:1200px;height:546px;
    background:radial-gradient(ellipse at 72% 45%,#5b4a3c 0%,#3a2e26 40%,#1f1915 100%)}
  .hero-photo{position:absolute;inset:0;background:linear-gradient(90deg,rgba(20,16,13,.55),rgba(20,16,13,.1) 60%,rgba(20,16,13,.5))}
  .account-bar{position:absolute;top:2px;right:83px;display:flex;height:44px}
  .account-bar a{display:flex;align-items:center;justify-content:center;width:138px;font-family:"Cinzel",Georgia,serif;font-size:14px;font-weight:600;text-decoration:none;color:var(--white)}
  .account-bar .my-account{background:#111}
  .account-bar .post-brief{background:var(--gold)}
  .hero-title{position:absolute;left:0;top:208px;width:1200px;text-align:center;font-family:"Cinzel",Georgia,serif;font-weight:600;font-size:30px;line-height:36px;color:var(--white)}
  .hero-title span{display:block;color:var(--gold-light)}
  .hero-btn{position:absolute;top:300px;height:58px;width:232px;border:2px solid var(--gold);display:flex;align-items:center;justify-content:center;gap:10px;font-family:"Cinzel",Georgia,serif;font-size:15px;font-weight:600;color:var(--white);text-decoration:none}
  .slider-dots{position:absolute;top:519px;left:542px;display:flex;gap:20px}
  .slider-dots i{width:9px;height:9px;border-radius:50%;border:2px solid var(--white);display:block}
  .slider-dots i.active{background:var(--gold);border-color:var(--gold)}

  /* issues */
  .issues{position:absolute;left:0;top:664px;width:1200px;height:489px;background:linear-gradient(120deg,#2b2624,#1d1a18 60%,#2c2725)}
  .issues-photo{position:absolute;left:0;top:0;width:418px;height:489px;background:linear-gradient(135deg,#5a3a28 0%,#7b4a2d 45%,#3d2519 100%)}
  .issues-title{position:absolute;left:466px;top:74px;font-family:"Cinzel",Georgia,serif;font-size:26px;font-weight:400;color:var(--white)}
  .issue-list{position:absolute;left:470px;top:135px;list-style:none;font-family:"Cinzel",Georgia,serif;font-size:14.5px;color:var(--white)}
  .issue-list li{height:32px;display:flex;align-items:center;gap:10px}
  .issue-list svg{flex:none}

  /* attorneys */
  .section-title{position:absolute;left:0;top:1209px;width:1200px;text-align:center;font-family:"Cinzel",Georgia,serif;font-size:25px;font-weight:600;color:var(--ink)}
  .section-title em{font-style:normal;color:var(--gold)}
  .advisor{position:absolute;top:1281px;width:225px}
  .advisor-photo{width:225px;height:193px;background:linear-gradient(160deg,#d2d2d2,#7a7a7a)}
  .advisor dl{margin-top:30px}
  .advisor dt{font-size:12.5px;color:var(--gold);height:18px}
  .advisor dd{font-family:"Cinzel",Georgia,serif;font-size:13.5px;font-weight:600;color:var(--ink);height:38px;white-space:nowrap}
  .stars{display:flex;gap:3px;margin-top:-2px}
  .advice-btn{position:absolute;top:557px;left:0;width:225px;height:48px;border:2px solid var(--gold);display:flex;align-items:center;justify-content:center;gap:12px;font-family:"Cinzel",Georgia,serif;font-size:14.5px;font-weight:600;color:var(--ink);text-decoration:none}

  /* footer links */
  .footer-links{position:absolute;left:0;top:1954px;width:1200px;height:334px;background:var(--cream)}
  .footer-links h3{position:absolute;top:50px;font-family:"Cinzel",Georgia,serif;font-size:18px;font-weight:700;color:var(--gold)}
  .footer-links ul{position:absolute;top:98px;list-style:none;font-size:12.5px;color:#2e2c2a}
  .footer-links li{height:26.5px;display:flex;align-items:center;gap:12px}
  .footer-links .chev li::before{content:"›";color:var(--gold);font-size:16px;line-height:1}

  .footer-bar{position:absolute;left:0;top:2288px;width:1200px;height:87px;background:var(--dark)}
  .copyright{position:absolute;left:81px;top:34px;font-family:"Cinzel",Georgia,serif;font-size:13px;color:var(--white)}
  .footer-mark{position:absolute;left:560px;top:28px;width:80px;text-align:center;font-family:"Cinzel",Georgia,serif;font-size:14px;font-weight:600;color:var(--gold)}
  .connect{position:absolute;right:83px;top:26px;display:flex;align-items:center;gap:10px;font-family:"Cinzel",Georgia,serif;font-size:13px;color:var(--white)}
  .connect i{width:27px;height:27px;border-radius:50%;background:var(--white);display:block}
  .footer-strip{position:absolute;left:0;top:2375px;width:1200px;height:54px;background:var(--gold);text-align:center;font-family:"Cinzel",Georgia,serif;font-size:24px;line-height:54px;color:var(--white)}
</style>
</head>
<body>

<header class="site-header">
  <div class="brand"><span class="brand-dot"></span>BriefHarbor</div>
  <nav class="main-nav">
    <a href="#" style="left:426px">Sectors</a>
    <a href="#" style="left:539px">Legal Advisors</a>
    <a href="#" style="left:706px">Browse Briefs</a>
    <a href="#" style="left:868px">How it works</a>
    <a href="#" style="left:1027px">Contact us</a>
  </nav>
</header>

<section class="hero">
  <div class="hero-photo" role="img" aria-label="Dim courtroom with bronze scales of justice"></div>
  <div class="account-bar">
    <a class="my-account" href="#">My Account</a>
    <a class="post-brief" href="#">Post a brief</a>
  </div>
  <h1 class="hero-title">Get numerous legal opinions on your case,<span>and select your most preferred legal advisor</span></h1>
  <a class="hero-btn" href="#" style="left:363px">Get started now
    <svg width="16" height="10" viewBox="0 0 16 10"><path d="M0 5h13M9 1l4 4-4 4" stroke="#fff" stroke-width="2" fill="none"/></svg></a>
  <a class="hero-btn" href="#" style="left:605px">See how it works</a>
  <div class="slider-dots"><i></i><i></i><i class="active"></i><i></i><i></i></div>
</section>

<section class="issues">
  <div class="issues-photo" role="img" aria-label="Warm wooden desk detail in close-up"></div>
  <h2 class="issues-title">What does your issue relate to?</h2>
  <ul class="issue-list">
    <li><svg width="12" height="12" viewBox="0 0 12 12"><circle cx="6" cy="6" r="6" fill="#c9962f"/><path d="M5 3.5 7.5 6 5 8.5" stroke="#262322" stroke-width="1.6" fill="none"/></svg>Purchase and supply of goods and/or services</li>
    <li><svg width="12" height="12" viewBox="0 0 12 12"><circle cx="6" cy="6" r="6" fill="#c9962f"/><path d="M5 3.5 7.5 6 5 8.5" stroke="#262322" stroke-width="1.6" fill="none"/></svg>Someone copying my work, ideas, identity, trade marks</li>
    <li><svg width="12" height="12" viewBox="0 0 12 12"><circle cx="6" cy="6" r="6" fill="#c9962f"/><path d="M5 3.5 7.5 6 5 8.5" stroke="#262322" stroke-width="1.6" fill="none"/></svg>Agreements or contracts</li>
    <li><svg width="12" height="12" viewBox="0 0 12 12"><circle cx="6" cy="6" r="6" fill="#c9962f"/><path d="M5 3.5 7.5 6 5 8.5" stroke="#262322" stroke-width="1.6" fill="none"/></svg>The relationship between employer and employee(s)</li>
    <li><svg width="12" height="12" viewBox="0 0 12 12"><circle cx="6" cy="6" r="6" fill="#c9962f"/><path d="M5 3.5 7.5 6 5 8.5" stroke="#262322" stroke-width="1.6" fill="none"/></svg>Injury to person, property or reputation</li>
    <li><svg width="12" height="12" viewBox="0 0 12 12"><circle cx="6" cy="6" r="6" fill="#c9962f"/><path d="M5 3.5 7.5 6 5 8.5" stroke="#262322" stroke-width="1.6" fill="none"/></svg>The duties of a government agency or department</li>
    <li><svg width="12" height="12" viewBox="0 0 12 12"><circle cx="6" cy="6" r="6" fill="#c9962f"/><path d="M5 3.5 7.5 6 5 8.5" stroke="#262322" stroke-width="1.6" fill="none"/></svg>Problems with property, land, business premises, apartments, flats, house</li>
    <li><svg width="12" height="12" viewBox="0 0 12 12"><circle cx="6" cy="6" r="6" fill="#c9962f"/><path d="M5 3.5 7.5 6 5 8.5" stroke="#262322" stroke-width="1.6" fill="none"/></svg>The content of a will, the operation of trusts, and/or the behaviour of trustees</li>
    <li><svg width="12" height="12" viewBox="0 0 12 12"><circle cx="6" cy="6" r="6" fill="#c9962f"/><path d="M5 3.5 7.5 6 5 8.5" stroke="#262322" stroke-width="1.6" fill="none"/></svg>Other</li>
  </ul>
</section>

<h2 class="section-title"><em>Our</em> Attorneys</h2>

<article class="advisor" style="left:81px">
  <div class="advisor-photo" role="img" aria-label="Portrait of advisor in barrister's robes"></div>
  <dl>
    <dt>Advisor:</dt><dd>Rowan Ellery</dd>
    <dt>Occupation:</dt><dd>Barrister</dd>
    <dt>BriefHarbor Level:</dt><dd>Barrister 1 year call</dd>
    <dt>Sector:</dt><dd>Commercial</dd>
    <dt>Briefs answered:</dt><dd>58</dd>
    <dt>Rating:</dt>
    <dd class="stars"><svg width="80" height="14" viewBox="0 0 80 14"><g fill="#1f1d1b"><path id="st" d="M7 0l2 4.6 5 .5-3.8 3.3 1.1 5L7 10.8 2.7 13.4l1.1-5L0 5.1l5-.5z"/><use href="#st" x="17"/><use href="#st" x="34"/><use href="#st" x="51"/></g></svg></dd>
  </dl>
  <a class="advice-btn" href="#">Ask me for advice <svg width="16" height="10" viewBox="0 0 16 10"><path d="M0 5h13M9 1l4 4-4 4" stroke="#1f1d1b" stroke-width="2" fill="none"/></svg></a>
</article>

<article class="advisor" style="left:351px">
  <div class="advisor-photo" role="img" aria-label="Advisor studying papers at a desk"></div>
  <dl>
    <dt>Advisor:</dt><dd>Tessa Wrenfield</dd>
    <dt>Occupation:</dt><dd>Student</dd>
    <dt>BriefHarbor Level:</dt><dd>Student</dd>
    <dt>Sector:</dt><dd>All</dd>
    <dt>Briefs answered:</dt><dd>2</dd>
    <dt>Rating:</dt>
    <dd class="stars"><svg width="97" height="14" viewBox="0 0 97 14"><g fill="#1f1d1b"><use href="#st"/><use href="#st" x="17"/><use href="#st" x="34"/><use href="#st" x="51"/><use href="#st" x="68"/></g></svg></dd>
  </dl>
  <a class="advice-btn" href="#">Ask me for advice <svg width="16" height="10" viewBox="0 0 16 10"><path d="M0 5h13M9 1l4 4-4 4" stroke="#1f1d1b" stroke-width="2" fill="none"/></svg></a>
</article>

<article class="advisor" style="left:622px">
  <div class="advisor-photo" role="img" aria-label="Portrait of advisor in a suit"></div>
  <dl>
    <dt>Advisor:</dt><dd>Miles Corrin</dd>
    <dt>Occupation:</dt><dd>Solicitor</dd>
    <dt>BriefHarbor Level:</dt><dd>Solicitor qualified for 6 yrs</dd>
    <dt>Sector:</dt><dd>Tort / Delict</dd>
    <dt>Briefs answered:</dt><dd>12</dd>
    <dt>Rating:</dt>
    <dd class="stars"><svg width="63" height="14" viewBox="0 0 63 14"><g fill="#1f1d1b"><use href="#st"/><use href="#st" x="17"/><use href="#st" x="34"/></g></svg></dd>
  </dl>
  <a class="advice-btn" href="#">Ask me for advice <svg width="16" height="10" viewBox="0 0 16 10"><path d="M0 5h13M9 1l4 4-4 4" stroke="#1f1d1b" stroke-width="2" fill="none"/></svg></a>
</article>

<article class="advisor" style="left:892px">
  <div class="advisor-photo" role="img" aria-label="Portrait of advisor with dark hair"></div>
  <dl>
    <dt>Advisor:</dt><dd>Anika Dorsey</dd>
    <dt>Occupation:</dt><dd>Solicitor</dd>
    <dt>BriefHarbor Level:</dt><dd>Solicitor qualified for 1 yr</dd>
    <dt>Sector:</dt><dd>Commercial, Property, Tax</dd>
    <dt>Briefs answered:</dt><dd>5</dd>
    <dt>Rating:</dt>
    <dd class="stars"><svg width="80" height="14" viewBox="0 0 80 14"><g fill="#1f1d1b"><use href="#st"/><use href="#st" x="17"/><use href="#st" x="34"/><use href="#st" x="51"/></g></svg></dd>
  </dl>
  <a class="advice-btn" href="#">Ask me for advice <svg width="16" height="10" viewBox="0 0 16 10"><path d="M0 5h13M9 1l4 4-4 4" stroke="#1f1d1b" stroke-width="2" fill="none"/></svg></a>
</article>

<footer class="footer-links">
  <h3 style="left:81px">I need a...</h3>
  <ul class="chev" style="left:81px">
    <li>Commercial Law Advisor</li>
    <li>Consumer Affairs Law Advisor</li>
    <li>Contract Law Advisor</li>
    <li>Intellectual Property Law Advisor</li>
    <li>Land / Property Law Advisor</li>
    <li>Equity, Wills &amp; Trusts Law Advisor</li>
  </ul>
  <ul class="chev" style="left:374px">
    <li>Public Law &amp; Judicial Review Advisor</li>
    <li>Employment Law Advisor</li>
    <li>Defamation Law Advisor</li>
    <li>Personal Injury Law Advisor</li>
    <li>All legal advice</li>
  </ul>
  <h3 style="left:717px">About us</h3>
  <ul style="left:717px">
    <li>About us</li>
    <li>How it works</li>
    <li>Contact Us</li>
    <li>Affiliate Programme?</li>
    <li>Media</li>
    <li>Help / FAQ</li>
    <li>Social Media</li>
  </ul>
  <h3 style="left:973px">Jurisdiction</h3>
  <ul style="left:973px">
    <li>Jurisdiction</li>
    <li>England &amp; Wales</li>
    <li>United States</li>
    <li>Scotland</li>
    <li>Australia</li>
    <li>Ireland</li>
    <li>A Judicial Committee</li>
    <li>of the Privy Council</li>
  </ul>
</footer>

<div class="footer-bar">
  <p class="copyright">© 2015 Copyrights. All Rights Reserved</p>
  <div class="footer-mark">BriefHarbor</div>
  <div class="connect">Connect with us :<i></i><i></i><i></i><i></i></div>
</div>
<div class="footer-strip">BriefHarbor</div>

</body>
</html>
```